Brochure Design Project

We need a brochure design.
It is an A3 page folded into 2 A4.
The brochure is for a company at the catering services in Israel - mostly finger food trays for businesses and home events.
Most of the brochure will be like a menu (we have the photos). To every photo there will be 3-4 short sentences that describes the food presented.
The brochure will be in Hebrew language (Right to Left) - We will do all the Language stuff but need an impressive design for the brochure.
The brochure should communicate quality and pleasent feelings.

Target Market(s)

1] Businesses Events - the person that orders food for Board meetings, courses, conventions - most of the time the secretaries.
2] Home Events - like birthdays, Celebrations - most of the time the mother orders the food

Industry/Entity Type

Catering

Requirements
Must have
• We have a logo and web site (so the main colors should communicate with it).
There are 5 categories: Main dishes, Salads, Deserts, Drinks, Extras

```html
<!DOCTYPE html>
<html lang="he">
<head>
<meta charset="utf-8">
<title>Catering Menu Brochure</title>
<link rel="stylesheet" href="https://fonts.googleapis.com/css2?family=Crimson+Text:wght@700&family=David+Libre:wght@400;500&display=swap">
<style>
:root{
  --bg:#ece9e4;
  --paper-light:#e4e4e6;
  --paper-dark:#b9babd;
  --panel:rgba(255,255,255,.38);
  --plum:#5a2f3c;
  --plum-soft:#7a4a57;
  --ink:#2a2326;
  --tray-dark:#3a2a22;
  --tray-mid:#8a5a3a;
  --bowl:#1e1c1c;
  --photo-frame:#ffffff;
}
*{box-sizing:border-box;margin:0;padding:0}
html,body{width:1200px;height:900px;overflow:hidden;background:var(--bg)}
.spread{position:absolute;left:40px;top:54px;width:1120px;height:792px;display:flex;box-shadow:0 10px 30px rgba(0,0,0,.25)}
.page{position:relative;width:560px;height:792px;background:radial-gradient(ellipse at 60% 45%,var(--paper-light),var(--paper-dark));overflow:hidden}
.page--left::after,.page--right::before{content:"";position:absolute;top:0;bottom:0;width:40px}
.page--left::after{right:0;background:linear-gradient(to right,rgba(0,0,0,0),rgba(0,0,0,.14))}
.page--right::before{left:0;background:linear-gradient(to left,rgba(0,0,0,0),rgba(0,0,0,.12))}
.panel{position:absolute;background:var(--panel);border-radius:18px;box-shadow:inset 0 0 0 1px rgba(255,255,255,.4)}
.cat-title{position:absolute;height:52px;display:flex;align-items:center;justify-content:center}
.cat-title svg{position:absolute;inset:0;width:100%;height:100%}
.cat-title span{position:relative;font-family:"Crimson Text",Georgia,serif;font-weight:700;font-size:17px;color:#fff;letter-spacing:.2px}
.desc{direction:rtl;text-align:right;font-family:"David Libre",serif;font-size:9.5px;line-height:1.3;color:var(--ink)}
.desc .price{font-weight:500}
.photo{border:4px solid var(--photo-frame);box-shadow:0 2px 5px rgba(0,0,0,.3);background:linear-gradient(160deg,var(--tray-mid),var(--tray-dark))}
.photo--bowl{border-radius:50%/45%;border:0;box-shadow:0 3px 5px rgba(0,0,0,.35);background:radial-gradient(ellipse at 50% 40%,#6f8a3a 0,#8c3b2c 45%,var(--bowl) 62%)}
.photo-card{background:#fff;padding:6px;box-shadow:0 2px 5px rgba(0,0,0,.25)}
.row-list{position:absolute;display:flex;flex-direction:column}
.row-item{display:flex;align-items:center;gap:10px;justify-content:flex-end}
.grid-item{display:flex;flex-direction:column;align-items:center;gap:8px;width:125px}
.grid-item .desc{width:118px}
.bottom-row{position:absolute;display:flex;gap:10px}
.col-grid{position:absolute;display:grid;grid-template-columns:125px 125px;column-gap:12px;row-gap:18px}
</style>
</head>
<body>
<main class="spread">

  <!-- Left page -->
  <section class="page page--left">
    <div class="panel" style="left:28px;top:115px;width:245px;height:425px"></div>
    <div class="cat-title" style="left:18px;top:92px;width:235px">
      <svg viewBox="0 0 235 52" preserveAspectRatio="none" aria-hidden="true"><path d="M6 18 C40 8 120 14 228 10 L232 30 C180 40 90 44 10 42 C2 34 2 24 6 18Z" fill="var(--plum)"/></svg>
      <span>Food Category 1</span>
    </div>
    <div class="row-list" style="left:38px;top:140px;width:225px;gap:14px">
      <div class="row-item"><p class="desc">מגש כריכונים טריים במילויים מגוונים<br>סלמון, גבינות ושמנת עם עשבי תיבול<br>מוכן להגשה, 18 יחידות<br><span class="price">מחיר: 128 ₪</span></p><div class="photo" style="width:90px;height:60px" role="img" aria-label="Tray of finger sandwiches"></div></div>
      <div class="row-item"><p class="desc">מגש כריכונים טריים במילויים מגוונים<br>סלמון, גבינות ושמנת עם עשבי תיבול<br>מוכן להגשה, 18 יחידות<br><span class="price">מחיר: 128 ₪</span></p><div class="photo" style="width:90px;height:60px" role="img" aria-label="Tray of stuffed rolls"></div></div>
      <div class="row-item"><p class="desc">מגש כריכונים טריים במילויים מגוונים<br>סלמון, גבינות ושמנת עם עשבי תיבול<br>מוכן להגשה, 18 יחידות<br><span class="price">מחיר: 128 ₪</span></p><div class="photo" style="width:90px;height:60px" role="img" aria-label="Tray of mini pastries"></div></div>
      <div class="row-item"><p class="desc">מגש כריכונים טריים במילויים מגוונים<br>סלמון, גבינות ושמנת עם עשבי תיבול<br>מוכן להגשה, 18 יחידות<br><span class="price">מחיר: 128 ₪</span></p><div class="photo" style="width:90px;height:60px" role="img" aria-label="Tray of canapés"></div></div>
      <div class="row-item"><p class="desc">מגש כריכונים טריים במילויים מגוונים<br>סלמון, גבינות ושמנת עם עשבי תיבול<br>מוכן להגשה, 18 יחידות<br><span class="price">מחיר: 128 ₪</span></p><div class="photo" style="width:90px;height:60px;border-radius:50%;background:radial-gradient(circle,#b0303a 40%,#e8e2dc 62%,#8d8d8d 70%)" role="img" aria-label="Platter of sliced cured meats"></div></div>
    </div>

    <div class="cat-title" style="left:300px;top:68px;width:235px">
      <svg viewBox="0 0 235 52" preserveAspectRatio="none" aria-hidden="true"><path d="M4 14 C60 6 150 12 230 8 L232 34 C170 42 80 40 8 44 C2 32 2 22 4 14Z" fill="var(--plum)"/></svg>
      <span>Food Category 3</span>
    </div>
    <div class="col-grid" style="left:290px;top:125px">
      <div class="grid-item"><div class="photo" style="width:110px;height:58px" role="img" aria-label="Tray of macarons"></div><p class="desc">מגש כריכונים טריים במילויים מגוונים<br>סלמון, גבינות ושמנת עם עשבי תיבול<br>מוכן להגשה, 18 יחידות<br><span class="price">מחיר: 128 ₪</span></p></div>
      <div class="grid-item"><div class="photo" style="width:110px;height:58px" role="img" aria-label="Tray of petit fours"></div><p class="desc">מגש כריכונים טריים במילויים מגוונים<br>סלמון, גבינות ושמנת עם עשבי תיבול<br>מוכן להגשה, 18 יחידות<br><span class="price">מחיר: 128 ₪</span></p></div>
      <div class="grid-item"><div class="photo" style="width:110px;height:58px" role="img" aria-label="Tray of cookies and bars"></div><p class="desc">מגש כריכונים טריים במילויים מגוונים<br>סלמון, גבינות ושמנת עם עשבי תיבול<br>מוכן להגשה, 18 יחידות<br><span class="price">מחיר: 128 ₪</span></p></div>
      <div class="grid-item"><div class="photo" style="width:110px;height:58px" role="img" aria-label="Tray of chocolate cakes"></div><p class="desc">מגש כריכונים טריים במילויים מגוונים<br>סלמון, גבינות ושמנת עם עשבי תיבול<br>מוכן להגשה, 18 יחידות<br><span class="price">מחיר: 128 ₪</span></p></div>
      <div class="grid-item"><div class="photo" style="width:110px;height:58px;background:linear-gradient(160deg,#d9a560,#8a5a3a)" role="img" aria-label="Tray of pastries"></div><p class="desc">מגש כריכונים טריים במילויים מגוונים<br>סלמון, גבינות ושמנת עם עשבי תיבול<br>מוכן להגשה, 18 יחידות<br><span class="price">מחיר: 128 ₪</span></p></div>
      <div class="grid-item"><div class="photo" style="width:110px;height:58px;border-radius:50%;background:radial-gradient(circle,#e0b040 20%,#c24a3a 40%,#6a9a3a 55%,#c9c9c9 68%)" role="img" aria-label="Platter of fresh fruit"></div><p class="desc">מגש כריכונים טריים במילויים מגוונים<br>סלמון, גבינות ושמנת עם עשבי תיבול<br>מוכן להגשה, 18 יחידות<br><span class="price">מחיר: 128 ₪</span></p></div>
    </div>

    <div class="bottom-row" style="left:25px;top:590px">
      <div class="grid-item"><div class="photo" style="width:110px;height:58px" role="img" aria-label="Tray of savoury bites"></div><p class="desc">מגש כריכונים טריים במילויים מגוונים<br>סלמון, גבינות ושמנת עם עשבי תיבול<br>מוכן להגשה, 18 יחידות<br><span class="price">מחיר: 128 ₪</span></p></div>
      <div class="grid-item"><div class="photo" style="width:110px;height:58px" role="img" aria-label="Tray of sushi rolls"></div><p class="desc">מגש כריכונים טריים במילויים מגוונים<br>סלמון, גבינות ושמנת עם עשבי תיבול<br>מוכן להגשה, 18 יחידות<br><span class="price">מחיר: 128 ₪</span></p></div>
      <div class="grid-item"><div class="photo" style="width:110px;height:58px" role="img" aria-label="Tray of mini sandwiches"></div><p class="desc">מגש כריכונים טריים במילויים מגוונים<br>סלמון, גבינות ושמנת עם עשבי תיבול<br>מוכן להגשה, 18 יחידות<br><span class="price">מחיר: 128 ₪</span></p></div>
      <div class="grid-item"><div class="photo" style="width:110px;height:58px" role="img" aria-label="Tray of filled croissants"></div><p class="desc">מגש כריכונים טריים במילויים מגוונים<br>סלמון, גבינות ושמנת עם עשבי תיבול<br>מוכן להגשה, 18 יחידות<br><span class="price">מחיר: 128 ₪</span></p></div>
    </div>
  </section>

  <!-- Right page -->
  <section class="page page--right">
    <div class="panel" style="left:40px;top:40px;width:490px;height:430px"></div>
    <div class="cat-title" style="left:40px;top:22px;width:230px">
      <svg viewBox="0 0 230 52" preserveAspectRatio="none" aria-hidden="true"><path d="M6 16 C60 8 150 12 226 10 L228 32 C160 42 80 42 8 42 C2 32 2 24 6 16Z" fill="var(--plum)"/></svg>
      <span>Food Category 4</span>
    </div>
    <div class="row-list" style="left:180px;top:72px;width:320px;gap:12px">
      <div class="row-item"><p class="desc">מגש כריכונים טריים במילויים מגוונים<br>סלמון, גבינות ושמנת עם עשבי תיבול<br>מוכן להגשה, 18 יחידות<br><span class="price">מחיר: 128 ₪</span></p><div class="photo-card"><div class="photo--bowl" style="width:84px;height:46px;border-radius:50%;background:radial-gradient(circle,#d8b040 20%,#c0503a 40%,#7aa040 55%,#cfcfcf 70%)" role="img" aria-label="Vegetable platter"></div></div></div>
      <div class="row-item"><p class="desc">מגש כריכונים טריים במילויים מגוונים<br>סלמון, גבינות ושמנת עם עשבי תיבול<br>מוכן להגשה, 18 יחידות<br><span class="price">מחיר: 128 ₪</span></p><div class="photo-card"><div class="photo photo--bowl" style="width:84px;height:46px" role="img" aria-label="Bowl of tomato salad"></div></div></div>
      <div class="row-item"><p class="desc">מגש כריכונים טריים במילויים מגוונים<br>סלמון, גבינות ושמנת עם עשבי תיבול<br>מוכן להגשה, 18 יחידות<br><span class="price">מחיר: 128 ₪</span></p><div class="photo-card"><div class="photo photo--bowl" style="width:84px;height:46px;background:radial-gradient(ellipse,#5f8a30 0,#4a6a2a 50%,var(--bowl) 62%)" role="img" aria-label="Bowl of green salad"></div></div></div>
      <div class="row-item"><p class="desc">מגש כריכונים טריים במילויים מגוונים<br>סלמון, גבינות ושמנת עם עשבי תיבול<br>מוכן להגשה, 18 יחידות<br><span class="price">מחיר: 128 ₪</span></p><div class="photo-card"><div class="photo photo--bowl" style="width:84px;height:46px;background:radial-gradient(ellipse,#9a9a4a 0,#6a7a3a 50%,var(--bowl) 62%)" role="img" aria-label="Bowl of grain salad"></div></div></div>
      <div class="row-item"><p class="desc">מגש כריכונים טריים במילויים מגוונים<br>סלמון, גבינות ושמנת עם עשבי תיבול<br>מוכן להגשה, 18 יחידות<br><span class="price">מחיר: 128 ₪</span></p><div class="photo-card"><div class="photo photo--bowl" style="width:84px;height:46px;background:radial-gradient(ellipse,#b04a30 0,#8a3a28 50%,var(--bowl) 62%)" role="img" aria-label="Bowl of roasted pepper salad"></div></div></div>
      <div class="row-item"><p class="desc">מגש כריכונים טריים במילויים מגוונים<br>סלמון, גבינות ושמנת עם עשבי תיבול<br>מוכן להגשה, 18 יחידות<br><span class="price">מחיר: 128 ₪</span></p><div class="photo-card"><div class="photo photo--bowl" style="width:84px;height:46px;background:radial-gradient(ellipse,#d8d0b8 0,#a89a80 50%,var(--bowl) 62%)" role="img" aria-label="Bowl of pasta salad"></div></div></div>
    </div>

    <div class="cat-title" style="left:290px;top:488px;width:240px">
      <svg viewBox="0 0 240 52" preserveAspectRatio="none" aria-hidden="true"><path d="M4 18 C70 8 160 12 236 12 L236 34 C170 42 80 44 8 40 C2 30 2 24 4 18Z" fill="var(--plum)"/></svg>
      <span>Food Category 2</span>
    </div>
    <div class="bottom-row" style="left:30px;top:560px">
      <div class="grid-item"><div class="photo" style="width:110px;height:58px" role="img" aria-label="Tray of sushi"></div><p class="desc">מגש כריכונים טריים במילויים מגוונים<br>סלמון, גבינות ושמנת עם עשבי תיבול<br>מוכן להגשה, 18 יחידות<br><span class="price">מחיר: 128 ₪</span></p></div>
      <div class="grid-item"><div class="photo" style="width:110px;height:58px" role="img" aria-label="Tray of baguette sandwiches"></div><p class="desc">מגש כריכונים טריים במילויים מגוונים<br>סלמון, גבינות ושמנת עם עשבי תיבול<br>מוכן להגשה, 18 יחידות<br><span class="price">מחיר: 128 ₪</span></p></div>
      <div class="grid-item"><div class="photo" style="width:110px;height:58px;background:linear-gradient(160deg,#e0c8a0,#2a2222)" role="img" aria-label="Tray of triangle sandwiches"></div><p class="desc">מגש כריכונים טריים במילויים מגוונים<br>סלמון, גבינות ושמנת עם עשבי תיבול<br>מוכן להגשה, 18 יחידות<br><span class="price">מחיר: 128 ₪</span></p></div>
      <div class="grid-item"><div class="photo" style="width:110px;height:58px;background:linear-gradient(160deg,#d9a560,#5a3a2a)" role="img" aria-label="Tray of baked rolls"></div><p class="desc">מגש כריכונים טריים במילויים מגוונים<br>סלמון, גבינות ושמנת עם עשבי תיבול<br>מוכן להגשה, 18 יחידות<br><span class="price">מחיר: 128 ₪</span></p></div>
    </div>
  </section>

</main>
</body>
</html>
```